Business Card for Musician

The company is called Velkor Music Entertainment and i am the director (Miles Tenney) . I would like a logo made along with a list of services i provide :

Rock Pop and Jazz Covers music for Weddings , Birthdays , Pubs, Bars and Restaurants

I provide Solo/Duo and Bands for these functions.

Another aspect is i teach guitar and do music workshops and compose music for television.

I want to go for something different than a photo of a guitar or singer..i like the idea of soundwaves and an ear. or ripples of sound like a music note (as a drop of water) and the sound rippling out..another idea is something with lighting (music lights) with different colours lighting up the name Velkor..however im open to any ideas. Thanks

Target Market(s)

General Public, Music Agents, Venue Owners. English Speaking..adults from 25-50

Industry/Entity Type

Business

Font styles to use
Sans Serif

Colors

Designer to choose colors to be used in the design.

Requirements
Must have
• All the points about what i do...
Nice to have
• Logo could emphasize the VEL in Velkor...
Should not have
• Not too busy please...Simple but gets the message across. NOthing obvious like a photo of a musician playing.

```html
<!DOCTYPE html>
<html lang="en">
<head>
<meta charset="utf-8">
<title>Velkor Music – Miles Tenney</title>
<link rel="stylesheet" href="https://fonts.googleapis.com/css2?family=Cabin:wght@400;700&display=swap">
<style>
  :root {
    --card-black: #0a0a0a;
    --page-white: #ffffff;
    --text-white: #ffffff;
    --accent-green: #66ee11;
    --accent-red: #ff3311;
    --rule-grey: #d8d8d8;
  }
  html, body {
    margin: 0;
    padding: 0;
    width: 1200px;
    height: 665px;
    overflow: hidden;
    background: var(--page-white);
  }
  .card {
    position: relative;
    width: 1165px;
    height: 665px;
    background: var(--card-black);
    font-family: "Cabin", "Gill Sans", sans-serif;
    color: var(--text-white);
  }
  .brand-name {
    position: absolute;
    left: 0;
    width: 1165px;
    top: 48px;
    margin: 0;
    text-align: center;
    font-size: 190px;
    font-weight: 700;
    line-height: 1;
    letter-spacing: 2px;
    color: var(--text-white);
  }
  .brand-tag {
    position: absolute;
    left: 815px;
    top: 268px;
    margin: 0;
    font-size: 58px;
    font-weight: 700;
    line-height: 1;
    color: var(--accent-green);
  }
  .director {
    position: absolute;
    left: 0;
    width: 1165px;
    top: 360px;
    margin: 0;
    text-align: center;
    font-size: 48px;
    font-weight: 700;
    line-height: 1;
  }
  .services {
    position: absolute;
    left: 0;
    width: 1165px;
    top: 476px;
    margin: 0;
    padding: 0;
    list-style: none;
    text-align: center;
    font-size: 27px;
    line-height: 37px;
  }
  .services li { display: inline-block; margin: 0 8px; }
  .services .wide { display: block; }
  .services li::before {
    content: "";
    display: inline-block;
    width: 16px;
    height: 16px;
    margin-right: 4px;
    border-radius: 50%;
    background: var(--accent-green);
    vertical-align: -2px;
  }
  .rule {
    position: absolute;
    left: 0;
    top: 587px;
    width: 1157px;
    height: 2px;
    background: var(--rule-grey);
  }
  .contact {
    position: absolute;
    left: 330px;
    top: 604px;
    margin: 0;
    font-size: 26px;
    line-height: 34px;
    white-space: nowrap;
  }
  .contact .label { color: var(--accent-red); }
</style>
</head>
<body>
  <div class="card">
    <h1 class="brand-name">Velkor</h1>
    <p class="brand-tag">Music</p>

    <h2 class="director">Miles Tenney</h2>

    <ul class="services">
      <li class="wide">rock, pop &amp; jazz covers - weddings, birthdays, bars &amp; restaurants</li>
      <li>guitar lessons</li>
      <li>music workshops</li>
      <li>composition</li>
    </ul>

    <div class="rule"></div>

    <p class="contact">
      <span class="label">m</span> 0412 555 308
      <span class="label">e</span> velkormusicentertainment@mailbox.com
    </p>
  </div>
</body>
</html>
```